The Open Compass Field Journeys Travel Brochure

I'm looking for a brochure design for a new travel product - The Open Compass Field Journeys, catering for students above 12 years old. Target audience are schools that do destination projects. Brochure to be read by head teacher, parents and students.

Brochure should be A4 in size, 4-6 pages. Format of brochure is hard cover (a folder) with inlet for flyers. Flyers for destinations will be updated from time to time.

Finished job needs to be converted to electronic format for website and email proposal usage.

Attached is text to be used on brochure. Order of section can be adjusted.

For "Elements of the trip", please understand the contents and explain/display it in a graphic form.

For flyer, please come out with a template that I can use for other destinations. The main elements - what's included, number of days, location for pictures, itinerary, educational focus, should be alterable. Attached are text for two sample destinations.
Also attached (tour itinerary example) a version of flyer that I like.

I'm attaching some pictures here. If you find more suitable pictures, please feel free to use them.

Reason: I'm extending the deadline of this project by 4 days, as I need to add details & photo of another travel specialist in personnel session (total of 3 members). Also, in view of the amount of work a designer has to do for this project, I'm giving you more time for submission. Please do not hesitate to be in touch should you need more than 4 days extension. Thank you.

Target Market(s)

Schools - especially the head teacher and parents, to send students above 12 years old to travel

Industry/Entity Type

Electronic

Requirements
Must have
• This is a travel brochure with education elements in it. Parents feel better when their children are travelling for a purpose and lead by responsible teachers/adults whom they can trust. So, the design has to emphasis that education elements and safety are our utmost priority.
Nice to have
• We specialise in environmental study. So, it is nice to have the environmental touch in the design.
Should not have
• Our target market segment is the Middle East, which can be quite sensitive to religion. I prefer not to have any religious related illustration on the design.

```html
<!DOCTYPE html>
<html lang="en">
<head>
<meta charset="utf-8">
<title>Cairo &amp; Lucor – The Open Compass Field Journeys</title>
<link href="https://fonts.googleapis.com/css2?family=Arimo:ital,wght@0,400;0,700;1,700&display=swap" rel="stylesheet">
<style>
:root{
  --navy:#1d3f6e;
  --ink:#1f1f1f;
  --muted:#4a4a4a;
  --sheet:#ffffff;
  --canvas:#ffffff;
  --edge:#b9bcc2;
}
*{box-sizing:border-box;margin:0;padding:0}
html,body{width:899px;height:1200px;overflow:hidden;background:var(--canvas)}
body{position:relative;font-family:'Arimo',Arial,sans-serif;color:var(--ink)}

.sheet{position:absolute;height:566px;background:var(--sheet);border:1px solid var(--edge);overflow:hidden}
.sheet--cover{left:11px;top:49px;width:442px}
.sheet--p2{left:455px;top:49px;width:434px}
.sheet--p3{left:11px;top:623px;width:442px}
.sheet--p4{left:455px;top:623px;width:434px}

.band-top{position:absolute;left:0;right:0;top:0;height:10px;background:var(--navy)}
.band-foot{position:absolute;left:0;right:0;bottom:0;height:10px;background:var(--navy);color:#fff;font-size:5px;font-weight:700;line-height:10px;padding-left:10px}

.thumb{position:absolute;left:27px;width:72px;height:70px}
.day{position:absolute;left:125px;right:20px}
.day h2{font-size:12px;font-weight:700;color:#222;margin-bottom:4px}
.day p{font-size:6px;line-height:7.8px;color:var(--muted)}

/* cover */
.hero{position:absolute;left:0;top:0;width:100%;height:244px;background:linear-gradient(180deg,#8fa8c4 0%,#b7c3cf 38%,#c9b08a 62%,#a88760 82%,#8a6c4a 100%)}
.brand{position:absolute;left:41px;top:13px;width:80px;height:36px;background:#fff;display:flex;align-items:center;justify-content:center;text-align:center;padding:3px;font-size:7px;line-height:8.5px;font-weight:700;color:var(--navy)}
.title{position:absolute;left:12px;top:255px;font-size:33px;font-weight:700;font-style:italic;color:#111;letter-spacing:-.3px}
.subjects{position:absolute;left:12px;top:309px;font-size:8.6px;line-height:11px;color:#555}
.subjects b{font-weight:700;color:#333}
.included{position:absolute;left:12px;top:382px;width:122px}
.included h3{font-size:7.5px;font-weight:700;margin-bottom:8px;color:#222}
.inc{display:flex;align-items:center;gap:9px;font-size:5.8px;line-height:6.6px;color:var(--muted);height:26px}
.inc svg{flex:0 0 11px}
.itinerary{position:absolute;left:141px;top:361px;width:292px;height:186px;background:var(--navy);color:#fff;padding:9px 10px;display:grid;grid-template-columns:1fr 1fr;column-gap:8px;font-size:6.3px;line-height:7.6px}
.itinerary b{display:block;font-size:6.5px;margin-top:8px}
.itinerary b:first-child{margin-top:0}

.address{position:absolute;left:0;right:0;top:496px;text-align:center;font-size:7px;line-height:9px;color:var(--muted)}
</style>
</head>
<body>

<section class="sheet sheet--cover">
  <div class="hero" role="img" aria-label="Photo of the Great Sphinx in front of a pyramid under a pale blue sky"></div>
  <div class="brand">The Open Compass Field Journeys</div>
  <h1 class="title">Cairo &amp; Lucor</h1>
  <div class="subjects">
    <div><b>Main focus subject:</b> History and Anthropology</div>
    <div><b>Related subjects:</b> Geography, Development Studies, Agriculture, Environmental Management</div>
    <div><b>Environmental focus:</b> Impact of climate change on the Nile river basin</div>
  </div>
  <div class="included">
    <h3>What's included in price:</h3>
    <div class="inc"><svg width="11" height="11" viewBox="0 0 10 10"><path d="M0.5 5.5h9M5 1l2 4.5-2 4M2 3.5l1 2-1 2" stroke="#333" stroke-width="1.2" fill="none"/></svg>Air Ticket</div>
    <div class="inc"><svg width="11" height="11" viewBox="0 0 10 10"><circle cx="5" cy="2.5" r="2" fill="#333"/><rect x="2" y="5" width="6" height="5" rx="1" fill="#333"/></svg>Full-time Tour Director</div>
    <div class="inc"><svg width="11" height="11" viewBox="0 0 10 10"><rect x="1" y="4" width="8" height="5" fill="#333"/><rect x="1" y="2" width="3" height="2" fill="#333"/></svg>All accommodation</div>
    <div class="inc"><svg width="11" height="11" viewBox="0 0 10 10"><path d="M2 1v8M4 1v4M6 1v8M8 1v4" stroke="#333" stroke-width="1.2"/></svg>Meals</div>
    <div class="inc"><svg width="11" height="11" viewBox="0 0 10 10"><rect x="0.5" y="3" width="9" height="5" rx="1" fill="#333"/></svg>Tours led by local expert<br>tour guides</div>
    <div class="inc"><svg width="11" height="11" viewBox="0 0 10 10"><rect x="1" y="3" width="8" height="4" rx="1" transform="rotate(-20 5 5)" fill="#333"/></svg>Entrance fees to attractions</div>
  </div>
  <div class="itinerary">
    <div>
      <b>Day 1: Arrival at Cairo</b>– Cairo city tour<br>– Pyramid and Sphinx
      <b>Day 2: Cairo Museum &amp;<br>&nbsp;&nbsp;&nbsp;&nbsp;&nbsp;&nbsp;&nbsp;&nbsp;&nbsp;&nbsp;&nbsp;&nbsp;Khan El Khalili Bazaar</b>– Cairo to Aswan by flight or train
      <b>Day 3: Embark on Nile Cruise</b>– Visit high dam<br>– Visit unfinished obelisk<br>– Visit Philae Temple
      <b>Day 4: Nile Cruise</b>– Visit Temple of Kom Ombo<br>– Visit Edfu Temple
    </div>
    <div>
      <b>Day 5: Nile Cruise</b>– Visit Temple of Karnak<br>– Visit Temple of Luxor
      <b>Day 6: Disembark from Nile Cruise</b>– Visit Luxor<br>– Colossi of Memnon<br>– Visit Valley of the Kings<br>– Visit Hatshepsut Temple
      <b>Day 7: Luxor</b>– Visit Colossi of Memnon<br>– Visit Valley of the King<br>– Visit Hatshepsut Temple<br>– Lucor to Cairo by train
      <b>Day 8: Depart for home</b>
    </div>
  </div>
</section>

<section class="sheet sheet--p2">
  <div class="band-top"></div>
  <div class="thumb" style="top:57px;background:linear-gradient(160deg,#6e5236,#b8946a 55%,#8a6a48)" role="img" aria-label="Photo of carved columns and statues inside the Egyptian Museum"></div>
  <article class="day" style="top:38px">
    <h2>Day 1 – Arrival at Cairo (L/D)</h2>
    <p>Ahlan! Welcome to historical EGYPT!<br>Upon arrival at Cairo Airport, you will be met and assisted through passport control. You will then travel to Giza to see the famous Sphinx and visit the Great Pyramids. Giza is the location of the Pyramid of Khufu (also known as the 'Great Pyramid' and the 'Pyramid of Cheops'), the somewhat smaller Pyramid of Khafre (or Kephren), and the relatively modest-sized Pyramid of Menkaure (or Mykerinus), along with a number of smaller satellite edifices known as 'Queens pyramids'. The Great Pyramid was the centrepiece of an elaborate complex, which included several small pyramids, five boat pits, a mortuary temple, a causeway, a valley temple, and many flat-roofed tombs for officials and some members of the royal family. After this, you continue on to Sakkara with lunch at a restaurant en route.<br>After lunch, visit the Step Pyramid of Djoser, the oldest pyramid in Egypt. Built by the great architect Imhotep, the Step Pyramid shows the evolution from mastaba type tombs to the pyramid form. Nearby are tombs of kings and nobles dating from the earliest dynasties of the Old Kingdom period. From here you go to the ancient capital of Memphis to see the Alabaster Sphinx and the colossal statue of Rameses II.<br>Overnight in Cairo.</p>
  </article>

  <div class="thumb" style="top:220px;height:89px;background:linear-gradient(170deg,#2e1f14,#7a5027 50%,#c08a45)" role="img" aria-label="Photo of a lantern-lit lane in the old bazaar"></div>
  <article class="day" style="top:230px">
    <h2>Day 2 – Cairo Museum &amp; Bazaar (B/D)</h2>
    <p>After breakfast, you will take a tour to the world famous Egyptian Museum with its 100,000 objects covering 4,000 years of ancient Egyptian civilization, including the treasures of Tutankhamen. You will then immerse into the old souq of Khan El Khalili bazaar. In the evening, have a sumptuous dinner before transfer to railway station for departure to Aswan on first class sleeper train.</p>
  </article>

  <div class="thumb" style="top:352px;height:87px;background:linear-gradient(180deg,#97b2cc 0%,#b9a383 45%,#a07850 100%)" role="img" aria-label="Photo of the stone walls of Philae Temple against blue sky"></div>
  <article class="day" style="top:349px">
    <h2>Day 3 – Aswan – Nile Cruise (B/L/D)</h2>
    <p>Upon arrival in Aswan, you will be transferred to the Nile Cruise terminal. Embark on your cruise, where you will be welcomed and briefed about your journey on the cruise. Sit back and relax for your tour of Aswan.<br>• High dam<br>The high dam is the largest rock-filled dam in the world and one of the most important engineering feats of the 20th century, an artificial lake Nasser, with a surface of 4000 sq km lies behind the dam.<br>• Unfinished obelisk<br>The unfinished obelisk is the largest known ancient obelisk, located in the northern region of the stone quarries of ancient Egypt in Aswan. It is unknown which pharaoh created this structure. It is nearly one third larger than any other ancient Egyptian obelisk. If finished it would have measured around 42 m (approximately 137 feet) and would have weighed nearly 1,200 tons.<br>• Philae Temple<br>Philae Temple was dismantled and reassembled (on Agilika island about 550 meters from its original home on Philae island) High Dam was being constructed. The temple, dedicated to the goddess Isis, is in a beautiful setting which has been landscaped to match its original site. Its various shrines and sanctuaries, include the Vestibule of Nectanebos I, which is used as the entrance to the island.<br>Overnight on Cruise.</p>
  </article>
  <div class="band-foot">Email: info@opencompass.ae &nbsp;|&nbsp; +971 4 555 0142</div>
</section>

<section class="sheet sheet--p3">
  <div class="band-top"></div>
  <div class="thumb" style="top:25px;width:87px;height:72px;background:linear-gradient(180deg,#a9c0d6 0%,#c8a675 50%,#9c7a4e 100%)" role="img" aria-label="Photo of the Edfu Temple pylon"></div>
  <article class="day" style="top:32px">
    <h2>Day 4 – Nile Cruise (B/L/D)</h2>
    <p>Breakfast on board.<br>You will sail towards Luxor via Kom Ombo, Edfu and Esna.<br>• Temple of Kom Ombo<br>This is an unusual double temple built during the Ptolemaic dynasty in the Egyptian town of Kom Ombo. Some additions to it were later made during the Roman period. The building is unique because its double design meant that there were courts, halls, sanctuaries and rooms duplicated for two sets of gods. The southern half of the temple was dedicated to the crocodile god Sobek, god of fertility and creator of the world with Hathor and Khonsu. Meanwhile, the northern part of the temple was dedicated to the falcon god Haroeris, also known as Horus the Elder.<br>• Edfu Temple<br>Two splendid granite statues of Horus, who was generally represented as a man with a falcon's head, mark the entrance of this temple which was constructed during the Ptolemaic period start in 237 BC. Follow by 18 columns with palm leaves / flowers and well preserved wall paintings are witnesses of the great wealth of the older days. After that, you will return to the Cruise and continue your journey to Luxor.<br>Overnight on Cruise.</p>
  </article>

  <div class="thumb" style="top:192px;width:87px;height:84px;background:linear-gradient(170deg,#d1c2a6,#a88a63 55%,#7e6345)" role="img" aria-label="Photo of carved columns and statues at Karnak"></div>
  <article class="day" style="top:200px">
    <h2>Day 5 – Nile Cruise – Luxor (B/L/D)</h2>
    <p>Today, you will be cruising into Luxor.<br>Upon arrival, you will be taken to visit the impressive temples of Karnak and Luxor.<br>• Temple of Karnak<br>It is the largest Temple in the World! The complex contains a group of temples such as the Great Temple of Amon Ra, The Temple of Khonso, The Ipt Temple, The Temple of Ptah, the Temple of Monthu and the Temple of the God Osiris. A 20m high, mud brick enclosure wall, surrounds all of these buildings.<br>• Temple of Luxor<br>It is close to the Nile and parallel with the riverbank. King Amenhotep III who reigned 1390-53 BC built this beautiful temple and dedicated it to Amon-Re, king of the gods, his consort Mut, and their son Khons.<br>This temple has been in almost continuous use as a place of worship right up to the present day. It was completed by Tutankhamun and Horemheb and added to by Rameses II. Towards the rear is a granite shrine dedicated to Alexander the Great.<br>Overnight on Cruise.</p>
  </article>

  <div class="thumb" style="top:311px;width:87px;height:90px;background:linear-gradient(160deg,#dcc7a0,#b38d5b 55%,#8e6a40)" role="img" aria-label="Photo of the terraced Hatshepsut Temple below cliffs"></div>
  <article class="day" style="top:323px">
    <h2>Day 6 – Luxor – Cairo (B/D)</h2>
    <p>After breakfast, you will disembark from the Nile Cruise and then visit the city of Luxor where you will see:<br>• Colossi of Memnon<br>The colossi are two massive stone statues of Pharaoh Amenhotep III. For the past 3400 years (since 1350 BC) they have stood in the Theban necropolis, across the River Nile from the modern city of Luxor.<br>• Valley of the Kings<br>The Valley of the Kings, less often called the Valley of the Gates of the Kings, is a valley in Egypt where, for a period of nearly 500 years from the 16th to 11th century BC, tombs were constructed for the Pharaohs and powerful nobles of the New Kingdom (the Eighteenth to the Twentieth Dynasties of Ancient Egypt). The valley stands on the West bank of the Nile, opposite Thebes (modern Luxor), within the heart of the Theban Necropolis. The wadi consists of two valleys, East Valley (where the majority of the royal tombs situated) and West Valley.<br>• Hatshepsut Temple<br>Hatshepsut, meaning Foremost of Noble Ladies (1508–1458 BC), was the fifth pharaoh of the eighteenth dynasty of Ancient Egypt. She is generally regarded by Egyptologists as one of the most successful pharaohs, reigning longer than any other woman of an indigenous Egyptian dynasty.<br>Transfer to Luxor station for sleeper train to Cairo.</p>
  </article>
  <div class="band-foot">Email: info@opencompass.ae &nbsp;|&nbsp; +971 4 555 0142</div>
</section>

<section class="sheet sheet--p4">
  <div class="band-top"></div>
  <div class="thumb" style="left:22px;top:25px;width:86px;height:97px;background:linear-gradient(180deg,#c9d3dc 0%,#b2a88e 45%,#7b7a62 100%)" role="img" aria-label="Photo of a domed building above a tree-lined Cairo street"></div>
  <article class="day" style="top:32px">
    <h2>Day 7 – Cairo (B)</h2>
    <p>Breakfast on train.<br>Today is your free day to wander around Cairo.<br>You may also choose to visit Alexandria, the beautiful port city at an extra cost of USD100 per person.</p>
  </article>

  <div class="thumb" style="left:22px;top:195px;width:86px;height:92px;background:linear-gradient(180deg,#d4dee6 0%,#9aa6ae 50%,#6d7a6a 100%)" role="img" aria-label="Photo of a large metal globe sculpture near the airport"></div>
  <article class="day" style="top:200px">
    <h2>Day 8 – Departure (B)</h2>
    <p>After breakfast, free and easy until time to transfer to airport for departure.</p>
  </article>

  <div class="address">
    Open Compass Travel Management<br>
    Suite 210 Harbour View Tower, Marina District,<br>
    PO Box 10234, Dubai, UAE<br>
    Tel: +971 4 555 0142 • Fax: +971 4 555 0199<br>
    Email: info@opencompass.ae
  </div>
  <div class="band-foot">Email: info@opencompass.ae &nbsp;|&nbsp; +971 4 555 0142</div>
</section>

</body>
</html>
```